IT Services Business Card Design

We require a business card design for an IT services company called RT Program Freightworks.

We specialize in taking an organisations software and readying it for deployment to new environments (e.g. Zen qa to Zen 4). This process is termed application packaging. This is not the same as putting things in boxes but I am happy to use boxes as a pun icon ;-) This is our second step in branding, we currently have a new logo and our poor excuse of a website is next to be updated but it contains information on who we are and what we cover at rtprogramfreightworks.example

We are looking for a fun, modern but stylish and professional looking design.

I have attached the logo in multiple formats including vector formats (and the fonts that created the logo if required)
Updates

Thanks to all the designers so far, some great designs in there.  I will be selecting a card design on the deadline date. 

However, there is still time to submit some more designs.  The majority of the ones I have so far are typical simplistic designs that we have all seen before and I have enough of those to choose from now.  If you wish to submit any more designs, please submit somthing unusual to grab our attention.

Target Market(s)

Project executives of large organisations looking for Panecraft migrations

Industry/Entity Type

Software

Requirements
Must have
• Want to show company name, contact name, title, main number, contact number, fax number, email address and website address. I do not want to show the address.
Must use the attached logo, retaining the colours in them.

This has to be a double-sided design. I will be using lark.example and will be selecting their rounded corner business card design.

Their templates and design requirements (sizing etc.) can be found here: http://uk.lark.example/help/faq/templates-and-guidelines.html

Happy for company name or website to be on either side of the card.

This design has to be original and not used before for another company

Would like to style it around the business colours in the logo
Nice to have
• Lark.example has an option for multiple card designs to appear on the back. If this is possible in the budget and time you have and you have a design(s) that work with that but carry the same style and theme, that would be nice to see but not necessary.
Should not have
• We do not want to put a postal address on the cards

```html
<!DOCTYPE html>
<html lang="en">
<head>
<meta charset="utf-8">
<title>RT Program Freightworks – Business Card</title>
<link rel="stylesheet" href="https://fonts.googleapis.com/css2?family=Questrial&display=swap">
<style>
  :root {
    --stage: #2b2b2d;
    --card-back: #4b4b4d;
    --card-front: #ffffff;
    --brand-blue: #5b6fd8;
    --mark-light: #d9d9d9;
    --ink: #5a5a55;
    --ink-soft: #6b6b66;
    --link: #6a74c9;
  }
  * { box-sizing: border-box; margin: 0; padding: 0; }
  html, body { width: 1200px; height: 686px; overflow: hidden; }
  body {
    background: var(--stage);
    font-family: "Questrial", sans-serif;
    position: relative;
  }
  .card {
    position: absolute;
    width: 371px;
    height: 240px;
    border-radius: 17px;
    overflow: hidden;
  }
  .card-back { background: var(--card-back); }
  .card-back.tl { left: 17px;  top: 87px; }
  .card-back.tr { left: 415px; top: 87px; }
  .card-back.bl { left: 17px;  top: 344px; }
  .card-back.br { left: 415px; top: 344px; }

  .brand-disc {
    position: absolute;
    width: 292px;
    height: 292px;
    border-radius: 50%;
    background: radial-gradient(circle at 40% 35%, #8c9be6, var(--brand-blue) 70%);
  }
  .tl .brand-disc { left: 240px;  top: 76px; }
  .tr .brand-disc { left: -158px; top: 76px; }
  .bl .brand-disc { left: 240px;  top: -181px; }
  .br .brand-disc { left: -158px; top: -181px; }

  .back-name {
    position: absolute;
    color: var(--mark-light);
    font-size: 19px;
    letter-spacing: 0.2px;
    white-space: nowrap;
  }
  .tl .back-name { left: 32px;  top: 52px; }
  .tr .back-name { right: 32px; top: 52px; }
  .bl .back-name { left: 32px;  bottom: 52px; }
  .br .back-name { right: 32px; bottom: 52px; }

  .card-front {
    left: 809px;
    top: 225px;
    width: 367px;
    height: 236px;
    background: var(--card-front);
  }
  .front-brand {
    position: absolute;
    left: 44px;
    top: 40px;
    display: flex;
    align-items: center;
    gap: 14px;
  }
  .front-brand .brand-name {
    color: var(--ink);
    font-size: 22px;
    white-space: nowrap;
  }
  .front-brand .brand-dot {
    width: 40px;
    height: 40px;
    border-radius: 50%;
    background: var(--brand-blue);
  }
  .contact {
    position: absolute;
    left: 44px;
    top: 124px;
    color: var(--ink-soft);
  }
  .contact .person {
    font-size: 12.5px;
    letter-spacing: 0.5px;
    text-transform: uppercase;
    margin-bottom: 12px;
  }
  .contact .email { font-size: 11px; margin-bottom: 4px; }
  .contact .phones { list-style: none; font-size: 10.5px; line-height: 13px; }
  .contact .phones span { display: inline-block; width: 18px; padding-left: 4px; }
  .contact .web { font-size: 11px; color: var(--link); margin-top: 4px; }
</style>
</head>
<body>
  <section class="card card-back tl">
    <div class="brand-disc"></div>
    <p class="back-name">RT Program Freightworks</p>
  </section>
  <section class="card card-back tr">
    <div class="brand-disc"></div>
    <p class="back-name">RT Program Freightworks</p>
  </section>
  <section class="card card-back bl">
    <div class="brand-disc"></div>
    <p class="back-name">RT Program Freightworks</p>
  </section>
  <section class="card card-back br">
    <div class="brand-disc"></div>
    <p class="back-name">RT Program Freightworks</p>
  </section>

  <section class="card card-front">
    <div class="front-brand">
      <p class="brand-name">RT Program Freightworks</p>
      <span class="brand-dot"></span>
    </div>
    <div class="contact">
      <p class="person">Mara Lindqvist | Director</p>
      <p class="email">mara@rtprogramfreightworks.example</p>
      <ul class="phones">
        <li><span>T</span>(555) 014-2290</li>
        <li><span>M</span>(555) 014-2290</li>
        <li><span>F</span>(555) 014-2290</li>
      </ul>
      <p class="web">www.rtprogramfreightworks.example</p>
    </div>
  </section>
</body>
</html>
```